Business Card

Can you please copy the format provided for the business cards.
Can the logo be in the colours of the last file as specified.

Can the text please be in grey

• Navy Blue: #00457C
• Grey Text: #555555
• Orange Text: #FDBF29

The names on the business card will be

Dorian Platt
0452 718 340
dorian.platt@ridgelineassetlending.com.au

Lvl 7, 14 Harbourview Pde
Merrivale QLD 4290
PO Box 3472
Tarrin Vale MC QLD 9781
P: 1300 462 519
F: 1300 462 538
www.ridgelineassetlending.com.au

And

Liam Hollis
0437 915 604
liam.hollis@ridgelineassetlending.com.au

Lvl 7, 14 Harbourview Pde
Merrivale QLD 4290
PO Box 3472
Tarrin Vale MC QLD 9781
P: 1300 462 519
F: 1300 471 926

Industry/Entity Type

Business

```html
<!DOCTYPE html>
<html lang="en">
<head>
<meta charset="utf-8">
<title>Ridgeline Asset Lending – Business Cards</title>
<link rel="stylesheet" href="https://fonts.googleapis.com/css2?family=Arimo:wght@400;700&display=swap">
<style>
  :root {
    --navy: #00457C;
    --grey-text: #555555;
    --dark-text: #444444;
    --orange: #FDBF29;
    --card-edge: #1e1e1e;
    --divider: #4a4a4a;
    --sheet: #ffffff;
  }
  * { box-sizing: border-box; margin: 0; padding: 0; }
  html, body {
    width: 1200px;
    height: 836px;
    overflow: hidden;
    background: var(--sheet);
    font-family: "Arimo", Arial, sans-serif;
  }
  .sheet { position: relative; width: 1200px; height: 836px; }

  .card {
    position: absolute;
    width: 546px;
    height: 304px;
    border: 2px solid var(--card-edge);
    background: var(--sheet);
    overflow: hidden;
  }
  .card--front.row-1 { left: 0; top: 45px; }
  .card--back.row-1  { left: 646px; top: 45px; }
  .card--front.row-2 { left: 0; top: 429px; }
  .card--back.row-2  { left: 646px; top: 429px; }

  address { font-style: normal; }

  /* Front */
  .brand-name {
    position: absolute;
    font-weight: 700;
    color: var(--navy);
    white-space: nowrap;
    letter-spacing: 0.2px;
  }
  .card--front .brand-name { left: 30px; top: 64px; font-size: 21px; }

  .tagline {
    position: absolute;
    right: 28px;
    top: 51px;
    text-align: right;
    font-size: 18px;
    font-weight: 700;
    line-height: 22px;
    letter-spacing: 0.3px;
    color: var(--dark-text);
  }
  .tagline .accent-navy { color: var(--navy); }
  .tagline .accent-orange { color: var(--orange); }

  .person {
    position: absolute;
    left: 26px;
    top: 219px;
    font-size: 14.5px;
    font-weight: 700;
    line-height: 20px;
    letter-spacing: 0.3px;
    color: var(--dark-text);
  }

  /* Back */
  .card--back .brand-name {
    left: 32px;
    top: 197px;
    font-size: 15px;
  }
  .divider {
    position: absolute;
    left: 228px;
    top: 90px;
    width: 4px;
    height: 164px;
    background: var(--divider);
  }
  .office {
    position: absolute;
    left: 243px;
    top: 109px;
    font-size: 13.5px;
    font-weight: 700;
    line-height: 18px;
    letter-spacing: 0.2px;
    color: var(--dark-text);
    white-space: nowrap;
  }
</style>
</head>
<body>
<main class="sheet">

  <section class="card card--front row-1">
    <div class="brand-name">Ridgeline Asset Lending</div>
    <p class="tagline">Smart <span class="accent-navy">LENDING</span><br>Steady <span class="accent-orange">GROWTH</span></p>
    <address class="person">
      Dorian Platt<br>
      0452 718 340<br>
      dorian.platt@ridgelineassetlending.com.au
    </address>
  </section>

  <section class="card card--back row-1">
    <div class="brand-name">Ridgeline Asset Lending</div>
    <span class="divider"></span>
    <address class="office">
      Lvl 7, 14 Harbourview Pde<br>
      Merrivale QLD 4290<br>
      PO Box 3472<br>
      Tarrin Vale MC QLD 9781<br>
      P: 1300 462 519<br>
      F: 1300 462 538<br>
      www.ridgelineassetlending.com.au
    </address>
  </section>

  <section class="card card--front row-2">
    <div class="brand-name">Ridgeline Asset Lending</div>
    <p class="tagline">Smart <span class="accent-navy">LENDING</span><br>Steady <span class="accent-orange">GROWTH</span></p>
    <address class="person">
      Liam Hollis<br>
      0437 915 604<br>
      liam.hollis@ridgelineassetlending.com.au
    </address>
  </section>

  <section class="card card--back row-2">
    <div class="brand-name">Ridgeline Asset Lending</div>
    <span class="divider"></span>
    <address class="office">
      Lvl 7, 14 Harbourview Pde<br>
      Merrivale QLD 4290<br>
      PO Box 3472<br>
      Tarrin Vale MC QLD 9781<br>
      P: 1300 462 519<br>
      F: 1300 471 926<br>
      www.ridgelineassetlending.com.au
    </address>
  </section>

</main>
</body>
</html>
```